Kelvane Plumbing Business cards

Company is Kelvane Plumbing.
name Dashel Morrowby, I am a plumber, drainer, gasfitter and roofer
Mobile: 0431 906 154
Email address: info@kelvaneplumbing.example (check out my website for some ideas)
Website: www.kelvaneplumbing.example
ABN: 82 916 203 471
LIC: 604517K

I am reliable all round plumber. I am a 24 hour emergency service. Kelvane Plumbing is a professional plumbing service in the Illawarra, South Coast, Southern Sydney and Southern Highland regions of NSW. We offer a 24 hour emergency service for piece of mind to our customers. Call us now to see how we can help you. Kelvane Plumbing approaches every job with attention to detail and excellent customer service. With our superior workmanship you can be confident that the job will be done right the first time around. You can rest assured with results that are guaranteed to last.

Target Market(s)

the general public

Contact Information for Business Card

look up website for some ideas something with similar colours to logo and new modern and to catch the eye.

Colors
fdfdfd
ffffff
000000
7f7f7f
aaaaaa
33a6d7
0492cd

Requirements
Must have
• all contact details
• company- Kelvane Plumbing
• name- Dashel Morrowby
• number mobile- 0431 906 154
• Email address- info@kelvaneplumbing.example
• Website- www.kelvaneplumbing.example
• ABN- 82 916 203 471
• LIC- 604517K

```html
<!DOCTYPE html>
<html lang="en">
<head>
<meta charset="utf-8">
<title>Kelvane Plumbing Business Cards</title>
<link href="https://fonts.googleapis.com/css2?family=Cabin:ital,wght@0,400;0,500;0,600;0,700;1,400&display=swap" rel="stylesheet">
<style>
  :root {
    --stage-blue: #0a9bd0;
    --card-dark: #1b1b1c;
    --brand-blue: #0492cd;
    --accent-blue: #33a6d7;
    --white: #ffffff;
    --off-white: #fdfdfd;
    --grey: #aaaaaa;
  }
  * { margin: 0; padding: 0; box-sizing: border-box; }
  html, body {
    width: 1200px; height: 1000px; overflow: hidden;
    background: var(--stage-blue);
    font-family: "Cabin", sans-serif;
  }
  .stage { position: relative; width: 1200px; height: 1000px; }
  .card {
    position: absolute; left: 265px; width: 670px;
    background: var(--card-dark);
    overflow: hidden;
  }
  .card-front { top: 60px; height: 408px; }
  .card-back { top: 530px; height: 410px; }
  .card-texture { position: absolute; inset: 0; background: var(--card-dark); }

  .front-wordmark {
    position: absolute; left: 0; right: 0; top: 178px;
    text-align: center;
    font-size: 46px; font-weight: 600; letter-spacing: 1px;
    color: var(--brand-blue);
  }

  .back-wordmark {
    position: absolute; left: 0; right: 0; top: 50px;
    text-align: center;
    font-size: 22px; font-weight: 600; letter-spacing: 0.5px;
    color: var(--brand-blue);
  }
  .holder-name {
    position: absolute; left: 0; right: 0; top: 172px;
    text-align: center;
    font-size: 50px; font-weight: 700;
    color: var(--white);
  }
  .holder-trades {
    position: absolute; left: 0; right: 0; top: 242px;
    text-align: center;
    font-size: 17px; font-style: italic;
    color: var(--accent-blue);
  }
  .contact-row {
    position: absolute; left: 25px; right: 25px; top: 316px;
    display: flex; justify-content: center; gap: 16px;
  }
  .contact-item {
    display: flex; align-items: center; gap: 7px;
    font-size: 14px; color: var(--off-white);
    white-space: nowrap;
  }
  .contact-icon { width: 34px; height: 34px; flex: none; }
  .registration-row {
    position: absolute; left: 0; right: 0; top: 370px;
    display: flex; justify-content: center; gap: 22px;
    font-size: 15px; font-weight: 500; color: var(--off-white);
  }
  .registration-label {
    color: var(--accent-blue); font-weight: 600; font-size: 18px; margin-right: 6px;
  }
</style>
</head>
<body>
<main class="stage">
  <section class="card card-front">
    <div class="card-texture" role="img" aria-label="Subtle dark tiled pattern of crossed wrenches"></div>
    <div class="front-wordmark">Kelvane Plumbing</div>
  </section>

  <section class="card card-back">
    <div class="card-texture" role="img" aria-label="Subtle dark tiled pattern of crossed wrenches"></div>
    <div class="back-wordmark">Kelvane Plumbing</div>
    <h1 class="holder-name">Dashel Morrowby</h1>
    <p class="holder-trades">Plumber | Drainer | Gasfitter | Roofer</p>

    <div class="contact-row">
      <div class="contact-item">
        <svg class="contact-icon" viewBox="0 0 36 36" aria-hidden="true">
          <circle cx="18" cy="18" r="16" fill="none" stroke="#0492cd" stroke-width="2"/>
          <path d="M12.5 10.5c1-.8 2-.6 2.6.3l1.5 2.3c.5.8.3 1.6-.4 2.2l-.9.7c.8 2 2.3 3.6 4.3 4.6l.8-.9c.6-.7 1.5-.8 2.2-.3l2.3 1.6c.8.6 1 1.7.2 2.6-1.6 1.8-3.6 1.9-5.9.6-3.4-1.9-6-5-7.3-8.5-.6-1.9-.6-3.7.6-5.2z" fill="#0492cd"/>
        </svg>
        <span>0431 906 154</span>
      </div>
      <div class="contact-item">
        <svg class="contact-icon" viewBox="0 0 36 36" aria-hidden="true">
          <circle cx="18" cy="18" r="16" fill="none" stroke="#0492cd" stroke-width="2"/>
          <text x="18" y="24" text-anchor="middle" font-family="Cabin, sans-serif" font-size="19" fill="#0492cd">@</text>
        </svg>
        <span>info@kelvaneplumbing.example</span>
      </div>
      <div class="contact-item">
        <svg class="contact-icon" viewBox="0 0 36 36" aria-hidden="true">
          <circle cx="18" cy="18" r="16" fill="none" stroke="#0492cd" stroke-width="2"/>
          <g fill="none" stroke="#0492cd" stroke-width="1.4">
            <circle cx="18" cy="18" r="9"/>
            <ellipse cx="18" cy="18" rx="4" ry="9"/>
            <line x1="9" y1="18" x2="27" y2="18"/>
            <line x1="10.5" y1="13.5" x2="25.5" y2="13.5"/>
            <line x1="10.5" y1="22.5" x2="25.5" y2="22.5"/>
          </g>
        </svg>
        <span>www.kelvaneplumbing.example</span>
      </div>
    </div>

    <div class="registration-row">
      <span><span class="registration-label">ABN</span>82 916 203 471</span>
      <span><span class="registration-label">LIC</span>604517K</span>
    </div>
  </section>
</main>
</body>
</html>
```